Carpentry and Building Business Card

I'm looking for a business card that is minimalistic and that incorporates the theme of my Velmor logo.
On one side I'd like the VELMOR logo with my details on the other side.
Double sided with curved edges

Target Market(s)

Construction / renovation
Adults

Industry/Entity Type

Tradesman

Contact Information for Business Card

Logo on one side, details on the other

Colors

Designer to choose only greyscale colors for use in the design.

Requirements
Must have
• Nilo Petrakis
VELMOR CONSTRUCT
Carpentry & Building Services
0481236574
Velmorconstruct@brixmail.com
Lic No. 718263D
Nice to have
• Fb and insta icons. @velmorconstruct
Should not have
• No hammer or tool icons please.

No address line.

```html
<!DOCTYPE html>
<html lang="en">
<head>
<meta charset="utf-8">
<title>Velmor Construct – Business Cards</title>
<link rel="stylesheet" href="https://fonts.googleapis.com/css2?family=Montserrat:wght@400;500;600&display=swap">
<style>
  :root {
    --backdrop: #2b2b2b;
    --grey-soft: #8c8c8c;
    --grey-deep: #5e5e5e;
    --grey-accent: #777777;
    --white: #ffffff;
    --ink: #1c1c1c;
  }
  * { margin: 0; padding: 0; box-sizing: border-box; }
  html, body { width: 1200px; height: 900px; overflow: hidden; }
  body {
    background: var(--backdrop);
    font-family: "Montserrat", sans-serif;
    position: relative;
  }
  .card {
    position: absolute;
    width: 514px;
    height: 296px;
    border-radius: 24px;
    overflow: hidden;
  }
  .card--front-soft   { left: 72px;  top: 138px; background: var(--grey-soft); }
  .card--front-deep   { left: 616px; top: 138px; background: var(--grey-deep); }
  .card--front-white  { left: 72px;  top: 465px; background: var(--white); }
  .card--details      { left: 616px; top: 465px; background: var(--white); }

  .wordmark {
    position: absolute;
    left: 51px;
    top: 217px;
    display: flex;
    align-items: center;
    gap: 14px;
  }
  .wordmark__square {
    width: 30px;
    height: 30px;
    background: var(--white);
  }
  .wordmark__name {
    font-size: 21px;
    font-weight: 400;
    letter-spacing: 4.5px;
    color: var(--white);
  }
  .card--front-white .wordmark__square { background: var(--grey-accent); }
  .card--front-white .wordmark__name { color: var(--ink); }

  .details__line {
    position: absolute;
    left: 43px;
    color: var(--ink);
    white-space: nowrap;
  }
  .details__name {
    top: 128px;
    font-size: 17px;
    line-height: 20px;
    font-weight: 600;
    color: var(--grey-accent);
  }
  .details__company { top: 158px; font-size: 13px; line-height: 15px; font-weight: 500; }
  .details__service { top: 173px; font-size: 13px; line-height: 15px; font-weight: 400; }
  .details__licence { top: 199px; font-size: 10px; line-height: 12px; }
  .details__rule {
    position: absolute;
    left: 43px;
    top: 222px;
    width: 26px;
    height: 2px;
    background: var(--ink);
  }
  .details__phone { top: 233px; font-size: 13.5px; line-height: 17px; }
  .details__email { top: 250px; font-size: 13.5px; line-height: 17px; }

  .social__item {
    position: absolute;
    left: 329px;
    display: flex;
    align-items: center;
    gap: 6px;
    font-size: 13.5px;
    line-height: 17px;
    color: var(--ink);
    white-space: nowrap;
  }
  .social__item--first  { top: 233px; }
  .social__item--second { top: 250px; }
  .social__dot {
    width: 10px;
    height: 10px;
    border-radius: 50%;
    background: var(--ink);
  }
</style>
</head>
<body>
  <section class="card card--front-soft">
    <div class="wordmark"><span class="wordmark__square"></span><span class="wordmark__name">VELMOR.</span></div>
  </section>

  <section class="card card--front-deep">
    <div class="wordmark"><span class="wordmark__square"></span><span class="wordmark__name">VELMOR.</span></div>
  </section>

  <section class="card card--front-white">
    <div class="wordmark"><span class="wordmark__square"></span><span class="wordmark__name">VELMOR.</span></div>
  </section>

  <section class="card card--details">
    <p class="details__line details__name">Nilo Petrakis</p>
    <p class="details__line details__company">VELMOR CONSTRUCT</p>
    <p class="details__line details__service">Carpentry &amp; Building Services</p>
    <p class="details__line details__licence">Lic No. 718263D</p>
    <div class="details__rule"></div>
    <p class="details__line details__phone">048.123.6574</p>
    <p class="details__line details__email">Velmorconstruct@brixmail.com</p>
    <p class="social__item social__item--first"><span class="social__dot"></span>velmorconstruct</p>
    <p class="social__item social__item--second"><span class="social__dot"></span>@velmorconstruct</p>
  </section>
</body>
</html>
```